a residential painting contractor I need a 6x9 postcard made

I already have a logo, I'm trying to offer my services to people. you can put that there's a 250$ discount for first time customers. include my License number #4627381 as well as the services I offer, interior and exterior painting, pressure washing, cabinet painting, epoxy floors, wood staining, decks, fences and much more. I'm licensed bonded and insured as well.

Target Market(s)

residential consumers (homeowners)

Industry/Entity Type

Painting contractor

Requirements
Must have
• postage stuff on the back I've linked some pictures top right please, my license number, what I do, phone number (555)317-0846 email velbrushworks7@mailzo.net, front and back of postcard
Nice to have
• well lit house in the background, maybe little circles of people doing some of the services I offer

```html
<!DOCTYPE html>
<html lang="en">
<head>
<meta charset="utf-8">
<title>Velbrush Works – Postcard Front and Back</title>
<link href="https://fonts.googleapis.com/css2?family=Lilita+One&family=Oswald:wght@500;700&family=Open+Sans:wght@400;700;800&display=swap" rel="stylesheet">
<style>
  :root {
    --bg: #d6d6d6;
    --ink: #161616;
    --white: #ffffff;
    --orange: #f39a1e;
    --blue: #1f5fb4;
    --blue-dark: #143f7c;
    --yellow: #ffc61a;
    --grey-line: #9a9a9a;
  }
  * { box-sizing: border-box; margin: 0; padding: 0; }
  html, body { width: 859px; height: 1200px; overflow: hidden; }
  body { background: var(--bg); font-family: "Open Sans", sans-serif; color: var(--ink); position: relative; }

  .postcard { position: absolute; left: 94px; width: 672px; height: 448px; overflow: hidden; box-shadow: 0 6px 18px rgba(0,0,0,.25); }
  .postcard--front { top: 92px; background: var(--ink); }
  .postcard--back { top: 668px; background: var(--white); }

  /* ---------- Front ---------- */
  .front-panel { position: absolute; inset: 14px; background: var(--white); }
  .brand { position: absolute; display: flex; align-items: center; gap: 6px; }
  .brand__dot { width: 22px; height: 22px; border-radius: 50%; background: var(--ink); flex: none; }
  .brand__name { font-family: "Open Sans", sans-serif; font-weight: 800; font-size: 13px; line-height: 1.05; color: var(--ink); text-transform: uppercase; }
  .front-panel .brand { left: 10px; top: 22px; width: 120px; }

  .headline { position: absolute; left: 170px; top: 22px; font-family: "Lilita One", sans-serif; font-size: 42px; line-height: 1.02; }
  .headline__top { color: var(--orange); display: block; }
  .headline__bottom { color: var(--blue); display: block; }

  .offer-ribbon { position: absolute; right: -14px; top: -14px; width: 150px; height: 150px; }

  .services-label { position: absolute; left: 0; top: 160px; width: 130px; height: 24px; background: var(--orange); color: var(--white); font-family: "Oswald", sans-serif; font-weight: 700; font-size: 14px; line-height: 24px; padding-left: 14px; letter-spacing: .4px; }
  .services { position: absolute; left: 12px; top: 192px; list-style: none; }
  .services li { font-weight: 800; font-size: 14px; line-height: 21.5px; display: flex; align-items: center; gap: 6px; }
  .services svg { width: 10px; height: 10px; flex: none; }

  .phone-pill { position: absolute; left: 8px; top: 342px; height: 38px; padding: 0 16px 0 8px; background: var(--blue); border-radius: 19px; display: flex; align-items: center; gap: 8px; color: var(--white); font-family: "Oswald", sans-serif; font-weight: 700; font-size: 21px; }
  .phone-pill__icon { width: 26px; height: 26px; border-radius: 50%; background: var(--white); display: flex; align-items: center; justify-content: center; }
  .phone-pill__icon svg { width: 14px; height: 14px; }

  .hero-photo { position: absolute; left: 236px; top: 126px; width: 408px; height: 294px; background: linear-gradient(160deg, #cfe3f4 0%, #d9c9a8 45%, #7c8c9a 100%); }

  /* ---------- Back ---------- */
  .credentials-bar { position: absolute; left: 0; top: 0; width: 322px; height: 54px; background: var(--ink); color: var(--white); font-family: "Oswald", sans-serif; font-weight: 700; font-size: 17px; line-height: 54px; padding-left: 22px; letter-spacing: .3px; }
  .about-shape, .estimate-shape { position: absolute; left: 0; }
  .about-shape { top: 88px; width: 350px; height: 200px; }
  .estimate-shape { top: 292px; width: 370px; height: 156px; }

  .about { position: absolute; left: 20px; top: 110px; width: 290px; color: var(--white); }
  .about__title { font-family: "Oswald", sans-serif; font-weight: 700; font-size: 18px; margin-bottom: 6px; }
  .about__text { font-size: 10.5px; line-height: 1.45; }

  .estimate { position: absolute; left: 22px; top: 316px; width: 300px; color: var(--white); }
  .estimate__title { font-family: "Oswald", sans-serif; font-weight: 700; font-size: 20px; }
  .estimate__phone { display: flex; align-items: center; gap: 8px; font-family: "Oswald", sans-serif; font-weight: 700; font-size: 28px; line-height: 1.1; }
  .estimate__phone svg { width: 20px; height: 20px; }
  .estimate__email { font-size: 12px; font-weight: 700; margin-top: 2px; }
  .license { display: inline-block; margin-top: 10px; background: var(--ink); color: var(--white); font-family: "Oswald", sans-serif; font-weight: 500; font-size: 12px; padding: 5px 12px; letter-spacing: .5px; }

  .postcard--back .brand { left: 440px; top: 40px; width: 140px; }
  .indicia { position: absolute; right: 16px; top: 14px; width: 66px; padding: 5px 2px; border: 1px solid var(--ink); text-align: center; font-size: 6.5px; font-weight: 700; line-height: 1.35; text-transform: uppercase; }
  .address { position: absolute; left: 420px; top: 206px; width: 220px; }
  .address__label { font-size: 9px; font-weight: 700; text-transform: uppercase; line-height: 1.35; margin-bottom: 10px; }
  .address__line { height: 1px; background: var(--grey-line); margin-bottom: 16px; }
</style>
</head>
<body>

<section class="postcard postcard--front" aria-label="Postcard front">
  <div class="front-panel">
    <div class="brand">
      <span class="brand__dot"></span>
      <span class="brand__name">Velbrush Works</span>
    </div>

    <h1 class="headline">
      <span class="headline__top">YOUR LOCAL</span>
      <span class="headline__bottom">PAINTING EXPERTS</span>
    </h1>

    <div class="hero-photo" role="img" aria-label="Bright house with a smiling painter holding a roller and colour swatches, plus small service scenes"></div>

    <div class="services-label">OUR SERVICES</div>
    <ul class="services">
      <li><svg viewBox="0 0 10 10"><path d="M1 1l4 4-4 4M5 1l4 4-4 4" fill="none" stroke="#1f5fb4" stroke-width="2"/></svg>Interior &amp; Exterior Painting</li>
      <li><svg viewBox="0 0 10 10"><path d="M1 1l4 4-4 4M5 1l4 4-4 4" fill="none" stroke="#1f5fb4" stroke-width="2"/></svg>Pressure Washing</li>
      <li><svg viewBox="0 0 10 10"><path d="M1 1l4 4-4 4M5 1l4 4-4 4" fill="none" stroke="#1f5fb4" stroke-width="2"/></svg>Cabinet Painting</li>
      <li><svg viewBox="0 0 10 10"><path d="M1 1l4 4-4 4M5 1l4 4-4 4" fill="none" stroke="#1f5fb4" stroke-width="2"/></svg>Epoxy Floors</li>
      <li><svg viewBox="0 0 10 10"><path d="M1 1l4 4-4 4M5 1l4 4-4 4" fill="none" stroke="#1f5fb4" stroke-width="2"/></svg>Wood Staining</li>
      <li><svg viewBox="0 0 10 10"><path d="M1 1l4 4-4 4M5 1l4 4-4 4" fill="none" stroke="#1f5fb4" stroke-width="2"/></svg>Decks &amp; Fences</li>
    </ul>

    <div class="phone-pill">
      <span class="phone-pill__icon"><svg viewBox="0 0 24 24"><path d="M6.6 10.8a15.2 15.2 0 0 0 6.6 6.6l2.2-2.2a1 1 0 0 1 1-.25 11.4 11.4 0 0 0 3.6.57 1 1 0 0 1 1 1V20a1 1 0 0 1-1 1A17 17 0 0 1 3 4a1 1 0 0 1 1-1h3.5a1 1 0 0 1 1 1c0 1.25.2 2.45.57 3.57a1 1 0 0 1-.25 1z" fill="#1f5fb4"/></svg></span>
      (555)317-0846
    </div>
  </div>

  <svg class="offer-ribbon" viewBox="0 0 150 150" aria-label="250 dollars off for first time customers">
    <polygon points="40,0 90,0 150,60 150,110" fill="#ffc61a"/>
    <g transform="translate(97 50) rotate(45)" text-anchor="middle" fill="#161616">
      <text y="0" font-family="Oswald, sans-serif" font-weight="700" font-size="20">250$ OFF</text>
      <text y="12" font-family="Open Sans, sans-serif" font-weight="700" font-size="7">FIRST TIME CUSTOMERS</text>
    </g>
  </svg>
</section>

<section class="postcard postcard--back" aria-label="Postcard back">
  <div class="credentials-bar">LICENSED BONDED AND INSURED</div>

  <svg class="about-shape" viewBox="0 0 350 200" preserveAspectRatio="none" aria-hidden="true">
    <path d="M0 0H300C330 30 345 70 320 110C300 150 330 180 350 200H0Z" fill="#f39a1e"/>
  </svg>
  <div class="about">
    <h2 class="about__title">ABOUT US</h2>
    <p class="about__text">We are a family run painting crew serving local homeowners with careful prep, clean lines and lasting finishes. From a single room to a full exterior, we treat every home like our own and leave it spotless when we finish.</p>
  </div>

  <svg class="estimate-shape" viewBox="0 0 370 156" preserveAspectRatio="none" aria-hidden="true">
    <path d="M0 10C90 0 200 20 290 8C340 30 360 90 370 156H0Z" fill="#1f5fb4"/>
  </svg>
  <div class="estimate">
    <div class="estimate__title">FREE ESTIMATE</div>
    <div class="estimate__phone">
      <svg viewBox="0 0 24 24"><path d="M6.6 10.8a15.2 15.2 0 0 0 6.6 6.6l2.2-2.2a1 1 0 0 1 1-.25 11.4 11.4 0 0 0 3.6.57 1 1 0 0 1 1 1V20a1 1 0 0 1-1 1A17 17 0 0 1 3 4a1 1 0 0 1 1-1h3.5a1 1 0 0 1 1 1c0 1.25.2 2.45.57 3.57a1 1 0 0 1-.25 1z" fill="#ffffff"/></svg>
      (555)317-0846
    </div>
    <div class="estimate__email">velbrushworks7@mailzo.net</div>
    <div class="license">LICENSE NUMBER #4627381</div>
  </div>

  <div class="brand">
    <span class="brand__dot"></span>
    <span class="brand__name">Velbrush Works</span>
  </div>

  <div class="indicia">PRSRT STD<br>ECRWSS<br>U.S. POSTAGE<br>PAID<br>EDDM RETAIL</div>

  <div class="address">
    <div class="address__label">Local Postal<br>Customer</div>
    <div class="address__line"></div>
    <div class="address__line"></div>
    <div class="address__line"></div>
  </div>
</section>

</body>
</html>
```